Portrait of a Learner Infographic

A portrait of a learner is an aspirational idea of the skills a student should have at graduation. "Learner" recognizes that learning continues after graduation.
An info graphic is needed to convey the skills that have been identified. A full version is needed that can be posted on classroom walls (11x17) and a simplified version to share on the website and any other means identified.
The Birchfield School District is in Concord, New Hampshire, the capital city for NH. The district serves 4,100 diverse students in seven schools and a regional career and technical education center.
The district's hex colors are Green: #007137 and Blue: #085bab
Each school has its own unique colors.
The design should be positive, aspirational and still professional.
Teachers, students and parents
Public school district

```html
<!DOCTYPE html>
<html lang="en">
<head>
<meta charset="utf-8">
<title>Birchfield School District – Portrait of a Learner</title>
<link href="https://fonts.googleapis.com/css2?family=Fjalla+One&family=Arimo:wght@400;700&display=swap" rel="stylesheet">
<style>
:root{
  --green:#007137;
  --green-dark:#005a2b;
  --blue:#085bab;
  --blue-deep:#0f5aa8;
  --paper:#f4f5f9;
  --ink:#111;
  --stage:#3a3a3a;
  --white:#fff;
}
*{box-sizing:border-box;margin:0;padding:0}
html,body{width:1200px;height:1200px;overflow:hidden;background:var(--stage)}
.poster{
  position:absolute;left:243px;top:53px;width:1148px;height:1760px;
  transform:scale(.621);transform-origin:0 0;
  background:var(--paper);overflow:hidden;
  font-family:"Arimo",Arial,sans-serif;color:var(--ink);
}
.shapes{position:absolute;left:0;top:0;width:1148px;height:1760px}
.brand{position:absolute;left:40px;top:70px;width:370px;display:flex;align-items:center;gap:14px}
.brand-dot{width:22px;height:22px;border-radius:50%;background:var(--blue);flex:none}
.brand-name{font-family:"Fjalla One",sans-serif;font-size:34px;line-height:1.1;color:var(--green)}
.divider{position:absolute;left:445px;top:30px;width:2px;height:135px;background:#ddd}
.district-title{position:absolute;left:535px;top:18px;font-family:"Fjalla One",sans-serif;font-size:46px;font-weight:400;color:var(--green)}
.mission{position:absolute;left:535px;top:86px;width:585px;font-size:19.5px;line-height:26px;text-align:justify}
.rule{position:absolute;left:55px;top:193px;width:1040px;height:3px;background:linear-gradient(90deg,transparent,#d5d5d5 20%,#d5d5d5 80%,transparent)}
.hero-title{position:absolute;left:0;width:1148px;top:208px;text-align:center;font-family:"Fjalla One",sans-serif;font-size:46px;font-weight:400;color:var(--white)}
.pillar{position:absolute;font-family:"Fjalla One",sans-serif;color:var(--white);font-size:34px;line-height:38px;text-align:center}
.card{position:absolute;width:287px;height:172px;border:3px solid var(--green);background:var(--white);overflow:hidden}
.card-head{height:66px;background:var(--green);display:flex;align-items:center;position:relative;margin:-3px -3px 0}
.card-icon{width:70px;height:66px;flex:none;display:flex;align-items:center;justify-content:center;background:var(--green-dark);clip-path:polygon(0 0,80% 0,100% 50%,80% 100%,0 100%)}
.card-icon svg{width:40px;height:40px}
.card-title{font-family:"Fjalla One",sans-serif;color:var(--white);font-size:24px;line-height:28px;padding-left:26px}
.card-body{font-size:16.5px;line-height:20px;text-align:center;padding:8px 8px 0}
.card-body p+p{margin-top:12px}
.card-body.dense{padding-top:4px;line-height:19px;text-align:justify;text-align-last:center}
.graduates{position:absolute;left:380px;top:1380px;width:410px;height:380px;border-radius:150px 150px 0 0;background:linear-gradient(180deg,#4a3a34 0%,#1f63b8 45%,#1b56a6 100%)}
</style>
</head>
<body>
<div class="poster">
  <svg class="shapes" viewBox="0 0 1148 1760" aria-hidden="true">
    <circle cx="571" cy="140" r="300" fill="none" stroke="var(--green)" stroke-width="9"/>
    <circle cx="571" cy="150" r="258" fill="none" stroke="var(--blue)" stroke-width="2.5" stroke-dasharray="4 5"/>
    <rect x="240" y="0" width="670" height="195" fill="var(--paper)"/>
    <path d="M341 195 A230 230 0 0 0 801 195 Z" fill="var(--blue)"/>
    <path d="M541 446 L601 446 L571 480 Z" fill="var(--green)"/>
    <path d="M330 340 L362 370 L325 370 Z M812 340 L780 370 L817 370 Z" fill="var(--green)"/>
    <path d="M505 305 L571 280 L645 305 L571 332 Z" fill="var(--white)"/>
    <path d="M530 318 L530 352 Q571 372 612 352 L612 318 L571 334 Z" fill="var(--white)"/>
    <path d="M518 312 L518 355" stroke="var(--white)" stroke-width="4"/>
    <circle cx="518" cy="360" r="7" fill="var(--white)"/>
    <path d="M85 282 Q150 255 205 262 L325 420 Q300 470 258 535 Q160 430 85 282 Z" fill="var(--blue-deep)"/>
    <path d="M1062 282 Q997 255 942 262 L818 420 Q846 470 890 535 Q988 430 1062 282 Z" fill="var(--blue-deep)"/>
    <path d="M420 570 Q571 540 722 570 L728 690 Q571 740 416 690 Z" fill="var(--blue-deep)"/>
    <g fill="var(--green)" stroke="var(--white)" stroke-width="7">
      <circle cx="208" cy="302" r="60"/>
      <circle cx="937" cy="302" r="60"/>
      <circle cx="571" cy="563" r="60"/>
    </g>
    <g fill="none" stroke="var(--white)" stroke-width="3" stroke-linecap="round">
      <path d="M185 330 V300 Q182 270 208 268 Q236 270 232 300 V330 Z M197 338 H221"/>
      <circle cx="231" cy="282" r="9"/>
      <circle cx="937" cy="292" r="13"/>
      <path d="M912 340 Q912 312 937 312 Q962 312 962 340 Z M937 262 V272 M910 292 H918 M956 292 H964 M918 272 L924 278 M956 272 L950 278"/>
      <path d="M538 570 L560 550 L578 560 L604 548 M538 570 L558 588 Q566 594 574 586 L600 566"/>
    </g>
    <g stroke="var(--green)" stroke-width="3" stroke-dasharray="4 5">
      <path d="M204 500 V1680"/>
      <path d="M575 700 V1313"/>
      <path d="M945 500 V1489"/>
    </g>
    <path d="M0 1660 Q300 1750 620 1700 Q880 1640 1148 1596 V1760 H0 Z" fill="var(--green)"/>
    <path d="M780 1640 Q960 1585 1148 1570 V1590 Q960 1600 790 1648 Z" fill="var(--blue)"/>
  </svg>

  <div class="brand"><span class="brand-dot"></span><span class="brand-name">Birchfield School District</span></div>
  <div class="divider"></div>
  <h1 class="district-title">Birchfield School District</h1>
  <p class="mission">Birchfield School District learners are informed, compassionate and capable citizens who effectively, courageously and responsibly direct their lives and positively impact communities</p>
  <div class="rule"></div>

  <h2 class="hero-title">Portrait of a Learner</h2>
  <div class="pillar" style="left:138px;top:380px;width:180px">Creative<br>&amp; Skillful</div>
  <div class="pillar" style="left:820px;top:380px;width:180px">Self-<br>Directed</div>
  <div class="pillar" style="left:430px;top:635px;width:286px">Collaborative</div>

  <div class="card" style="left:56px;top:557px"><div class="card-head"><div class="card-icon"><svg viewBox="0 0 40 40" fill="none" stroke="#fff" stroke-width="2"><path d="M12 34 V26 Q6 22 8 14 Q12 5 22 6 Q32 8 32 18 L35 24 H31 V30 H24 V34"/><circle cx="21" cy="17" r="5"/></svg></div><div class="card-title">Critical and<br>analytical thinker</div></div><div class="card-body">Accesses, evaluates, applies and communicates diverse forms of information for a variety of audiences and purposes</div></div>
  <div class="card" style="left:56px;top:747px"><div class="card-head"><div class="card-icon"><svg viewBox="0 0 40 40" fill="none" stroke="#fff" stroke-width="2"><path d="M14 26 Q8 20 10 13 Q14 5 20 5 Q26 5 30 13 Q32 20 26 26 V31 H14 Z M16 35 H24"/><path d="M21 11 L17 19 H23 L19 26"/></svg></div><div class="card-title">Innovative</div></div><div class="card-body">Makes productive and innovative decisions based on new learning that move an idea from concept to application</div></div>
  <div class="card" style="left:56px;top:938px"><div class="card-head"><div class="card-icon"><svg viewBox="0 0 40 40" fill="none" stroke="#fff" stroke-width="2"><circle cx="13" cy="13" r="6"/><path d="M26 7 L33 20 H19 Z M26 12 V15"/><path d="M5 32 L14 28 L26 30 L35 25"/></svg></div><div class="card-title">Informed risk-taker</div></div><div class="card-body">Gains awareness of relevant technology and practices that enable production in a variety of fields</div></div>
  <div class="card" style="left:56px;top:1128px"><div class="card-head"><div class="card-icon"><svg viewBox="0 0 40 40" fill="none" stroke="#fff" stroke-width="2"><circle cx="20" cy="15" r="9"/><circle cx="20" cy="15" r="3"/><path d="M5 33 L14 29 L26 31 L35 26"/></svg></div><div class="card-title">Adaptable</div></div><div class="card-body">Learns processes that enable individuals and collaborative teams to plan, design, test, execute, evaluate, reflect and adapt</div></div>
  <div class="card" style="left:56px;top:1318px"><div class="card-head"><div class="card-icon"><svg viewBox="0 0 40 40" fill="none" stroke="#fff" stroke-width="2"><circle cx="20" cy="19" r="13"/><path d="M16 15 Q16 10 20 10 Q25 10 24 15 Q23 18 20 20 V23 M20 27 V28"/></svg></div><div class="card-title">Curious</div></div><div class="card-body">Uses evidence of successes and challenges to adapt practices or processes in a manner that supports future growth</div></div>
  <div class="card" style="left:56px;top:1509px"><div class="card-head"><div class="card-icon"><svg viewBox="0 0 40 40" fill="none" stroke="#fff" stroke-width="2"><path d="M12 34 V26 Q6 22 8 14 Q12 5 22 6 Q32 8 32 18 L35 24 H31 V30 H24 V34"/><path d="M16 22 V14 M16 14 L13 17 M16 14 L19 17 M23 22 V12 M23 12 L20 15 M23 12 L26 15"/></svg></div><div class="card-title">Self-motivated</div></div><div class="card-body">Applies content knowledge to form creative inferences or provide innovative solutions</div></div>

  <div class="card" style="left:430px;top:762px"><div class="card-head"><div class="card-icon"><svg viewBox="0 0 40 40" fill="none" stroke="#fff" stroke-width="2"><path d="M12 34 V26 Q6 22 8 14 Q12 5 22 6 Q32 8 32 18 L35 24 H31 V30 H24 V34"/><circle cx="18" cy="14" r="4"/><circle cx="23" cy="14" r="4"/><circle cx="20" cy="19" r="4"/></svg></div><div class="card-title">Emotional<br>intelligence</div></div><div class="card-body"><p>Respectfully engages with others</p><p>Asks challenging and probing questions in a manner that preserves healthy relationships</p></div></div>
  <div class="card" style="left:430px;top:952px"><div class="card-head"><div class="card-icon"><svg viewBox="0 0 40 40" fill="none" stroke="#fff" stroke-width="2"><circle cx="20" cy="9" r="4"/><path d="M14 20 Q14 14 20 14 Q26 14 26 20 M6 18 V28 L14 35 M34 18 V28 L26 35 M10 22 L15 28 M30 22 L25 28"/></svg></div><div class="card-title">Civic minded</div></div><div class="card-body dense">Speaks and acts inclusively to support equity, safety and belonging with actions and behaviors that support an environment where all feel safe to learn and engage</div></div>
  <div class="card" style="left:430px;top:1142px"><div class="card-head"><div class="card-icon"><svg viewBox="0 0 40 40" fill="none" stroke="#fff" stroke-width="2"><path d="M12 34 V26 Q6 22 8 14 Q12 5 22 6 Q32 8 32 18 L35 24 H31 V30 H24 V34"/><path d="M21 22 L15 16 Q13 12 17 11 Q20 11 21 14 Q22 11 25 11 Q29 12 27 16 Z"/></svg></div><div class="card-title">Compassionate<br>leader</div></div><div class="card-body">Demonstrates and advocates for positive and sustainable change for oneself and others</div></div>

  <div class="card" style="left:798px;top:557px"><div class="card-head"><div class="card-icon"><svg viewBox="0 0 40 40" fill="none" stroke="#fff" stroke-width="2"><circle cx="13" cy="11" r="5"/><circle cx="25" cy="18" r="5"/><path d="M22 18 L24 20 L28 16 M5 32 L14 28 L26 30 L35 25"/></svg></div><div class="card-title">Responsible</div></div><div class="card-body">Understands own strengths, needs and interests</div></div>
  <div class="card" style="left:798px;top:747px"><div class="card-head"><div class="card-icon"><svg viewBox="0 0 40 40" fill="none" stroke="#fff" stroke-width="2"><path d="M14 26 Q8 20 10 13 Q14 5 20 5 Q26 5 30 13 Q32 20 26 26 V31 H14 Z M16 35 H24"/><path d="M15 14 H20 V10 M25 14 V19"/></svg></div><div class="card-title">Problem solver</div></div><div class="card-body">Accesses credible resources and seeks help to support growth and create actionable plans</div></div>
  <div class="card" style="left:798px;top:938px"><div class="card-head"><div class="card-icon"><svg viewBox="0 0 40 40" fill="none" stroke="#fff" stroke-width="2"><path d="M12 34 V26 Q6 22 8 14 Q12 5 22 6 Q32 8 32 18 L35 24 H31 V30 H24 V34"/><path d="M22 10 L17 18 H23 L19 25"/></svg></div><div class="card-title">Self-starter</div></div><div class="card-body">Uses effective time management, planning and communication to accomplish long and short-term goals</div></div>
  <div class="card" style="left:798px;top:1128px"><div class="card-head"><div class="card-icon"><svg viewBox="0 0 40 40" fill="none" stroke="#fff" stroke-width="2"><path d="M12 34 V26 Q6 22 8 14 Q12 5 22 6 Q32 8 32 18 L35 24 H31 V30 H24 V34"/><path d="M16 12 Q13 16 16 20 M19 11 V21 M23 16 H29"/></svg></div><div class="card-title">Resilient</div></div><div class="card-body">Perseveres through challenges and seeking new experiences</div></div>
  <div class="card" style="left:798px;top:1318px"><div class="card-head"><div class="card-icon"><svg viewBox="0 0 40 40" fill="none" stroke="#fff" stroke-width="2"><path d="M12 34 V26 Q6 22 8 14 Q12 5 22 6 Q32 8 32 18 L35 24 H31 V30 H24 V34"/><path d="M14 21 L19 16 L22 19 L28 12 M24 12 H28 V16"/></svg></div><div class="card-title">Growth mindset</div></div><div class="card-body">Approaches problems as opportunities and generates solutions</div></div>

  <div class="graduates" role="img" aria-label="Illustration of two smiling graduates in blue gowns and caps holding diplomas"></div>
</div>
</body>
</html>
```